Menu Design for Indian Restaurant

We are a new Indian restaurant, named Saffron Lantern Restaurant, looking for a sophisticated looking menu. It is a semi-formal dining restaurant with wooden tables and chairs and will have a focus on a creating a lively atmosphere. Environment-friendly products will be used, and the menu will be 100% vegetarian. There will be an emphasis on fresh, healthy and delicious food. We will be targeting vegans, vegetarians, health conscious people, people from all age groups, Indians, Australian's as well as other ethnic communities. We need a clean, simple, sophisticated design for the new restaurant menu. Attached is the restaurant logo for reference.

UPDATE:
- We have attached the menu
- We are not looking for any particular type of layout or size (open to suggests). Please suggest this after having a look at the menu contents. However, we will be having one formal menu to be used in the restaurant, and one in brochure form for distribution.
- There are no images at present. If you feel the need of images, please use sample images for now.

Thank you for the entries thus far.
Updates

Target Market(s)

All age groups from different nationalities

Industry/Entity Type

Indian Restaurant

Colors

Designer to choose colors to be used in the design.

Requirements
Nice to have
• This will be printed on environmentally friendly paper.

```html
<!DOCTYPE html>
<html lang="en">
<head>
<meta charset="utf-8">
<title>Saffron Lantern Restaurant – Breakfast Menu</title>
<link href="https://fonts.googleapis.com/css2?family=Open+Sans:wght@400&family=Roboto+Condensed:wght@300;400&display=swap" rel="stylesheet">
<style>
  :root {
    --page-bg: #ffffff;
    --board: #352b2b;
    --saffron: #f7993a;
    --leaf: #158c45;
    --text-light: #ffffff;
  }
  html, body {
    margin: 0;
    padding: 0;
    width: 1200px;
    height: 1200px;
    overflow: hidden;
    background: var(--page-bg);
  }
  .menu-sheet {
    position: relative;
    width: 1200px;
    height: 1200px;
  }
  .menu-shapes {
    position: absolute;
    inset: 0;
    width: 1200px;
    height: 1200px;
  }
  .menu-column {
    position: absolute;
    width: 340px;
    color: var(--text-light);
  }
  .menu-column--saffron { left: 254px; top: 155px; }
  .menu-column--leaf { left: 645px; top: 396px; }
  .section-title {
    margin: 0 0 14px 0;
    font-family: "Open Sans", sans-serif;
    font-weight: 400;
    font-size: 15.5px;
    line-height: 20px;
  }
  .dish-list {
    list-style: none;
    margin: 0;
    padding: 0;
  }
  .dish {
    margin: 0 0 9px 1px;
    font-family: "Roboto Condensed", sans-serif;
    font-weight: 300;
    font-size: 13.6px;
    line-height: 20px;
  }
</style>
</head>
<body>
<main class="menu-sheet">
  <svg class="menu-shapes" viewBox="0 0 1500 1500" xmlns="http://www.w3.org/2000/svg">
    <defs>
      <linearGradient id="curry-tones" x1="0" y1="0" x2="1" y2="1">
        <stop offset="0" stop-color="#c4452a"/>
        <stop offset="0.5" stop-color="#d8643a"/>
        <stop offset="1" stop-color="#a8321f"/>
      </linearGradient>
      <radialGradient id="dosa-tones" cx="0.45" cy="0.4" r="0.65">
        <stop offset="0" stop-color="#c99a5c"/>
        <stop offset="0.6" stop-color="#b78443"/>
        <stop offset="1" stop-color="#d9c24a"/>
      </radialGradient>
    </defs>
    <rect class="board" x="236" y="17" width="1038" height="1467" fill="var(--board)"/>
    <path class="panel-saffron" fill="var(--saffron)"
      d="M284,1465 L284,210 C284,110 370,25 470,25 L920,25 C820,45 750,140 750,255 L750,1140 C740,1320 660,1430 580,1465 Z"/>
    <path class="panel-leaf" fill="var(--leaf)"
      d="M775,1120 L775,260 C775,130 870,25 1005,25 L1020,25 C1140,25 1240,120 1240,260 L1240,1235 C1200,1350 1100,1440 1000,1465 L700,1465 C705,1445 698,1425 695,1415 C760,1350 775,1230 775,1120 Z"/>
    <path class="photo-curry" role="img" aria-label="Photo of a spiced red curry dish garnished with herbs"
      fill="url(#curry-tones)"
      d="M292,1187 L738,1187 L738,1240 C720,1350 650,1430 575,1455 L292,1455 Z"/>
    <circle class="photo-dosa" role="img" aria-label="Photo of a crisp dosa served with potato masala and chutneys"
      cx="1000" cy="255" r="218" fill="url(#dosa-tones)"/>
  </svg>

  <section class="menu-column menu-column--saffron">
    <h2 class="section-title">Breakfast</h2>
    <ul class="dish-list">
      <li class="dish">Dosa, Vada, Idly serve with sambar (Lentil) cocunut chutney<br>and tommato chilie chutney.</li>
      <li class="dish">Cris[y crepe made with ground ricelentils gluten free&nbsp; Rava<br>Dosa</li>
      <li class="dish">Dosa, Vada, Idly serve with sambar (Lentil) cocunut chutney<br>and tommato chilie chutney.</li>
      <li class="dish">Cris[y crepe made with ground ricelentils gluten free&nbsp; Rava<br>Dosa</li>
      <li class="dish">Dosa, Vada, Idly serve with sambar (Lentil) cocunut chutney<br>and tommato chilie chutney.</li>
      <li class="dish">Cris[y crepe made with ground ricelentils gluten free&nbsp; Rava<br>Dosa</li>
      <li class="dish">Dosa, Vada, Idly serve with sambar (Lentil) cocunut chutney<br>and tommato chilie chutney.</li>
      <li class="dish">Cris[y crepe made with ground ricelentils gluten free&nbsp; Rava<br>Dosa</li>
      <li class="dish">Dosa, Vada, Idly serve with sambar (Lentil) cocunut chutney<br>and tommato chilie chutney.</li>
      <li class="dish">Cris[y crepe made with ground ricelentils gluten free&nbsp; Rava<br>Dosa</li>
      <li class="dish">Dosa, Vada, Idly serve with sambar (Lentil) cocunut chutney<br>and tommato chilie chutney.</li>
      <li class="dish">Cris[y crepe made with ground ricelentils gluten free&nbsp; Rava<br>Dosa</li>
    </ul>
  </section>

  <section class="menu-column menu-column--leaf">
    <h2 class="section-title">Breakfast</h2>
    <ul class="dish-list">
      <li class="dish">Dosa, Vada, Idly serve with sambar (Lentil) cocunut chutney<br>and tommato chilie chutney.</li>
      <li class="dish">Cris[y crepe made with ground ricelentils gluten free&nbsp; Rava<br>Dosa</li>
      <li class="dish">Dosa, Vada, Idly serve with sambar (Lentil) cocunut chutney<br>and tommato chilie chutney.</li>
      <li class="dish">Cris[y crepe made with ground ricelentils gluten free&nbsp; Rava<br>Dosa</li>
      <li class="dish">Dosa, Vada, Idly serve with sambar (Lentil) cocunut chutney<br>and tommato chilie chutney.</li>
      <li class="dish">Cris[y crepe made with ground ricelentils gluten free&nbsp; Rava<br>Dosa</li>
      <li class="dish">Dosa, Vada, Idly serve with sambar (Lentil) cocunut chutney<br>and tommato chilie chutney.</li>
      <li class="dish">Cris[y crepe made with ground ricelentils gluten free&nbsp; Rava<br>Dosa</li>
      <li class="dish">Dosa, Vada, Idly serve with sambar (Lentil) cocunut chutney<br>and tommato chilie chutney.</li>
      <li class="dish">Cris[y crepe made with ground ricelentils gluten free&nbsp; Rava<br>Dosa</li>
      <li class="dish">Dosa, Vada, Idly serve with sambar (Lentil) cocunut chutney<br>and tommato chilie chutney.</li>
      <li class="dish">Cris[y crepe made with ground ricelentils gluten free&nbsp; Rava<br>Dosa</li>
    </ul>
  </section>
</main>
</body>
</html>
```